Legal Agribusiness Capability Brochure Design

Design A4 sized 6 page Legal Agribusiness Capability Brochure. Design is to be consistent with current marketing materials - logo, letterhead, website and business card to be provided.
Cover page - Firm name and logo, Agribusiness Capability Statement heading with image 1 below
Inside cover page - About Us section with image 2 below then Awards section below image
Inside middle page - Our Expertise with image 3 below
Inside back page - Our Experience with image 4 below
Back page - Senior Lawyers with image 5 below
Outside Middle Back Page - Contact Us with image 6
Updates

To provide more details to designers for brochure

Target Market(s)

Agribusiness - Australia

Industry/Entity Type

Legal

Colors

Designer to choose colors to be used in the design.

Requirements
Must have
• Use content from uloaded file - Agribusiness Brochure Content
• Use images uploaded
• Professional appearance
• Consistent with current marketing and website https://ferngatelegal.com.au/

```html
<!DOCTYPE html>
<html lang="en">
<head>
<meta charset="utf-8">
<title>Ferngate Legal – Agribusiness Capability Statement</title>
<link href="https://fonts.googleapis.com/css2?family=Open+Sans:ital,wght@0,300;0,400;0,600;0,700;1,400&display=swap" rel="stylesheet">
<style>
  :root{
    --stage:#8a8e96;
    --paper:#f7f7f7;
    --brand:#1a73c8;
    --brand-light:#3d9be0;
    --ink:#2b2b2b;
    --muted:#555b63;
    --gold:#e0b12a;
    --red:#d8252c;
    --sky-top:#a9d3ea;
    --sky-mid:#c7e3f2;
    --wheat:#e8a81c;
    --wheat-deep:#c9820c;
  }
  *{box-sizing:border-box;margin:0;padding:0}
  html,body{width:1096px;height:1200px;overflow:hidden}
  body{background:var(--stage);font-family:"Open Sans",Arial,sans-serif;color:var(--ink);position:relative}

  .spread{position:absolute;left:148px;width:800px;height:566px;box-shadow:0 10px 30px rgba(0,0,0,.28);overflow:hidden}
  .spread--outside{top:22px}
  .spread--inside{top:612px;background:var(--paper)}
  .page{position:absolute;top:0;width:400px;height:566px}
  .page--left{left:0}
  .page--right{left:400px}
  .fold{position:absolute;left:399px;top:0;width:2px;height:566px;background:linear-gradient(90deg,rgba(0,0,0,.12),rgba(255,255,255,.25))}

  /* outside spread */
  .sky-field{position:absolute;inset:0;background:linear-gradient(180deg,var(--sky-top) 0%,var(--sky-mid) 52%,#f3e3a6 66%,var(--wheat) 78%,var(--wheat-deep) 100%)}
  .intro{position:absolute;left:60px;top:42px;width:290px;font-size:6.4px;line-height:1.55;font-style:italic;color:#3b4a57;text-align:right}
  .office{position:absolute;right:50px;width:170px;text-align:right;font-size:6.4px;line-height:1.55;font-style:italic;color:#33414d}
  .office h3{font-style:normal;font-size:7.5px;font-weight:700;color:var(--brand);letter-spacing:.3px;margin-bottom:3px}
  .office--geraldton{top:140px}
  .office--perth{top:225px}
  .brand{display:flex;align-items:center;gap:7px}
  .brand__mark{width:18px;height:18px;background:var(--brand);border-radius:3px}
  .brand__name{font-weight:700;color:var(--brand);letter-spacing:.5px;text-transform:uppercase}
  .brand--back{position:absolute;left:96px;top:318px}
  .brand--back .brand__name{font-size:16px}
  .web-back{position:absolute;left:98px;top:346px;font-size:7.5px;letter-spacing:2.6px;color:#2c3a46;font-weight:600}
  .brand--cover{position:absolute;right:42px;top:58px}
  .brand--cover .brand__mark{width:26px;height:26px}
  .brand--cover .brand__name{font-size:21px}
  .cover-title{position:absolute;left:110px;top:128px;font-size:24px;line-height:1.2;font-weight:300;color:var(--brand-light);letter-spacing:1.5px}
  .badge{position:absolute;border-radius:50%;border:3px solid var(--gold);background:rgba(255,255,255,.25)}
  .badge--cover{left:170px;top:228px;width:72px;height:72px}
  .cover-ranked{position:absolute;left:70px;top:318px;width:300px;font-size:11px;font-weight:700;line-height:1.4;color:#1d2227}

  /* inside spread */
  .photo{position:absolute}
  .photo--pen{left:0;top:0;width:150px;height:78px;background:linear-gradient(135deg,#f1f1f1,#c9c9c9 60%,#8d8a86)}
  .photo--office{left:150px;top:0;width:130px;height:92px;background:linear-gradient(180deg,#8fbbe0,#6f8a72 55%,#3e5a3a)}
  .photo--aerial{left:280px;top:0;width:120px;height:108px;background:linear-gradient(150deg,#9fb7a8,#5f8f72 45%,#c5cbb9)}
  .photo--field{left:0;top:0;width:400px;height:128px;background:linear-gradient(180deg,#6f8fb6 0%,#d6d9cf 30%,#5f8c37 52%,#3f6d25 75%,#a0512b 100%)}
  .photo--harvest{left:0;top:432px;width:400px;height:90px;background:linear-gradient(180deg,#b9b2a4 0%,#8f7a5c 40%,#e1b83b 70%,#5b4a30 100%)}

  .col{position:absolute;font-size:6.2px;line-height:1.42;color:var(--muted)}
  .col h2{font-size:8.5px;font-weight:700;color:var(--brand);letter-spacing:.2px;margin-bottom:4px;text-transform:uppercase}
  .col h3{font-size:7.8px;font-weight:600;color:var(--brand);margin:6px 0 3px}
  .col h4{font-size:7.5px;font-weight:600;color:var(--red);margin:6px 0 2px}
  .col p{margin-bottom:3px;text-align:justify}
  .list{list-style:none}
  .list li{position:relative;padding-left:10px;margin-bottom:2px;text-align:justify}
  .list li::before{content:"";position:absolute;left:1px;top:3px;width:4px;height:4px;border-radius:50%;background:var(--brand)}
  .col--pragmatic{left:22px;top:94px;width:178px}
  .col--senior{left:214px;top:118px;width:166px}
  .membership-badge{width:60px;height:18px;border:1px solid #c9c9c9;background:#fff;margin-top:3px}
  .badge--inside{left:56px;top:290px;width:64px;height:64px;background:transparent}

  .band{position:absolute;left:0;width:400px}
  .band--people{top:388px;height:178px}
  .people-title{position:absolute;left:26px;top:408px;font-size:20px;font-weight:300;color:#fff;letter-spacing:.5px}
  .people-text{position:absolute;left:26px;top:442px;width:164px;font-size:6.2px;line-height:1.5;color:#eaf4fc;font-style:italic}
  .people-list{position:absolute;left:200px;top:440px;width:184px;list-style:none;font-size:6.3px;line-height:1.55;color:#fff}
  .people-list li{position:relative;padding-left:10px}
  .people-list li::before{content:"";position:absolute;left:0;top:3px;width:5px;height:5px;border-radius:50%;background:var(--gold)}
  .pageno{position:absolute;bottom:12px;width:18px;height:11px;border-radius:2px;background:var(--brand-light);color:#fff;font-size:6px;text-align:center;line-height:11px}
  .pageno--left{left:16px;background:#fff;color:var(--brand)}
  .pageno--right{right:16px}
  .web-inside{position:absolute;bottom:12px;font-size:6.5px;letter-spacing:1.5px;color:#fff}
  .web-inside--left{right:24px}
  .web-inside--right{left:30px}

  .col--exp-a{left:16px;top:138px;width:182px}
  .col--exp-b{left:208px;top:138px;width:180px}
</style>
</head>
<body>

<section class="spread spread--outside">
  <div class="sky-field" role="img" aria-label="Photograph of a golden wheat field under a pale blue sky with soft clouds, running across both pages"></div>

  <article class="page page--left back-page">
    <p class="intro">Our senior lawyers offer clients over 50 years of combined legal experience in a broad range of commercial law matters which has largely been developed from practising at reputable and long standing law firms in Perth and Fremantle. Our experience ensures that we are able to cater for client needs across our service areas whether it be in documenting and reviewing contracts, advising on disputes or representing clients in court.</p>

    <div class="office office--geraldton">
      <h3>GERALDTON OFFICE</h3>
      Suite 2, Saltbush House,<br>14 Harbour Lane,<br>Geraldton WA 6530<br>Phone: +61 8 9900 1234<br>Fax: +61 8 9900 1235<br>Email: info@ferngatelegal.com.au
    </div>
    <div class="office office--perth">
      <h3>PERTH OFFICE</h3>
      82 Calder Street<br>West Perth WA 6005<br>Phone: +61 8 9300 5670<br>Fax: +61 8 9300 5671<br>Email: info@ferngatelegal.com.au
    </div>

    <div class="brand brand--back"><span class="brand__mark"></span><span class="brand__name">Ferngate Legal</span></div>
    <div class="web-back">www.ferngatelegal.com.au</div>
  </article>

  <article class="page page--right cover-page">
    <div class="brand brand--cover"><span class="brand__mark"></span><span class="brand__name">Ferngate Legal</span></div>
    <h1 class="cover-title">AGRIBUSINESS<br>CAPABILITY<br>STATEMENT</h1>
    <div class="badge badge--cover" aria-hidden="true"></div>
    <p class="cover-ranked">Ranked as a leading agribusiness law firm<br>in Western Australia by Harlow's Guide</p>
  </article>
  <div class="fold"></div>
</section>

<section class="spread spread--inside">
  <article class="page page--left">
    <div class="photo photo--pen" role="img" aria-label="Close photograph of a hand signing a document with a pen"></div>
    <div class="photo photo--office" role="img" aria-label="Photograph of the firm's office building"></div>
    <div class="photo photo--aerial" role="img" aria-label="Aerial photograph of the coastal town and farmland"></div>

    <div class="col col--pragmatic">
      <h2>Pragmatic Legal Solutions</h2>
      <p>We take great pride in delivering quality and pragmatic legal advice to our clients. We focus on the process of delivering advice to our clients in order to achieve the desired outcome through:</p>
      <ul class="list">
        <li>senior lawyers with strong technical expertise advising clients without the duplication and costs often associated with multiple lawyers of varying experience working on the client's file;</li>
        <li>reducing operating costs without compromising on the quality of services delivered to clients; and</li>
        <li>adopting internal procedures, systems and information technology to promote efficiency.</li>
      </ul>
    </div>

    <div class="badge badge--inside" aria-hidden="true"></div>

    <div class="col col--senior">
      <h2>Senior Lawyers</h2>
      <p>Our senior lawyers all:</p>
      <ul class="list">
        <li>have no less than 10 years post admission experience;</li>
        <li>have strong technical expertise in their practice areas; and</li>
        <li>have acted or act as principals, directors, partners, consultants or senior associates in well-respected law firms in Perth.</li>
      </ul>
      <h3>Direct Access to Senior Lawyers</h3>
      <p>Clients, together with their accountants, financial planners, bankers and other consultants, are given direct access to our senior lawyers, to ensure that every client receives high-level advice.</p>
      <p>We provide direct and ongoing partner level involvement to each client to ensure that we deliver legal services at the level which our clients expect and deserve.</p>
      <h4>Memberships</h4>
      <p>Ferngate Legal is a member of the State Legal Practitioners Council.</p>
      <div class="membership-badge" aria-hidden="true"></div>
    </div>

    <svg class="band band--people" viewBox="0 0 400 178" preserveAspectRatio="none" aria-hidden="true">
      <defs><linearGradient id="peopleBlue" x1="0" x2="1" y1="0" y2="0"><stop offset="0" stop-color="#1565b8"/><stop offset="1" stop-color="#3fa3e3"/></linearGradient></defs>
      <path d="M0 10 Q200 -6 400 26 L400 178 L0 178 Z" fill="url(#peopleBlue)"/>
      <path d="M180 46 Q290 42 390 58" stroke="#5cb4ee" stroke-width="4" fill="none"/>
    </svg>
    <h2 class="people-title">Our People</h2>
    <p class="people-text">Ferngate Legal values the contribution of its people – our people are our assets. We have a small yet experienced team of professionals who are committed to delivering quality services to all clients at all times. We understand that relationships are built on trust. We build trust with our clients through:</p>
    <ul class="people-list">
      <li>Commitment to our clients;</li>
      <li>Open, honest and frank communication with our clients;</li>
      <li>Establishing long term relationships with our clients;</li>
      <li>Delivering quality legal solutions to our clients;</li>
      <li>Empathy towards our client's position and objectives;</li>
      <li>Working with integrity;</li>
      <li>Making our team accessible to our clients.</li>
    </ul>
    <span class="pageno pageno--left">2</span>
    <span class="web-inside web-inside--left">www.ferngatelegal.com.au</span>
  </article>

  <article class="page page--right">
    <div class="photo photo--field" role="img" aria-label="Photograph of green crop fields beside a red dirt road under a bright sky"></div>

    <div class="col col--exp-a">
      <p>Over the years our senior lawyers have acted for clients involved in wheat, canola, lupin, wool, beef, dairy, wool, lamb, poultry, piggery, viticulture, forestry and plantation operations. Our senior lawyers have strong family connections with various agribusiness operators which allows them to better appreciate the challenges faced in agribusiness.</p>
      <p>We can assist with the following agribusiness and rural matters:</p>
      <ul class="list">
        <li>Agribusiness and rural property contracts, agreements and deeds;</li>
        <li>Sale and purchase of farmland, agribusiness assets and livestock, including due diligence, pre-contractual negotiations, contract preparation, contract review and settlement;</li>
        <li>Rural and agribusiness succession planning, including intergenerational farm transfers and Family Farm Exemption transfers under the Duties Act 2008 (WA);</li>
        <li>Restructuring to facilitate succession planning;</li>
        <li>Farm Leases, Share Farming Agreements and Livestock Management Agreements;</li>
        <li>Pastoral leases and dealings with the Pastoral Lands Board;</li>
        <li>Foreign Investment Review Board (FIRB) advice and applications;</li>
        <li>Farm subdivisions;</li>
      </ul>
    </div>
    <div class="col col--exp-b">
      <ul class="list">
        <li>Land dealings with mining, energy and telecommunications companies, including lease and licence agreements, wind farm agreements, royalty agreements, land access agreements, compensation agreements and easement deeds;</li>
        <li>Compulsory acquisitions and land valuation matters;</li>
        <li>Structuring advice on issues relating to trading entities, partnerships, trusts, corporations, joint ventures, syndicates and family restructures;</li>
        <li>Trust deeds for holding and trading entities;</li>
        <li>Preparation of partnership agreements;</li>
        <li>Property ownership agreements;</li>
        <li>Preparation of trust deeds for holding and trading entities;</li>
        <li>Mortgages, crop liens and other securities against rural and agribusiness assets;</li>
        <li>Water rights, access and licences under the Waterways Conservation Act 1976 (WA);</li>
        <li>Carbon trading agreements;</li>
        <li>Employment Agreements;</li>
        <li>Contractor Agreements; and</li>
        <li>Litigation.</li>
      </ul>
    </div>

    <div class="photo photo--harvest" role="img" aria-label="Photograph of a yellow combine harvester cutting through a ripe wheat crop"></div>
    <svg class="band" style="top:504px;height:62px" viewBox="0 0 400 62" preserveAspectRatio="none" aria-hidden="true">
      <path d="M0 28 Q200 10 400 0 L400 62 L0 62 Z" fill="#2f8fdb"/>
      <path d="M0 24 Q200 6 400 -4" stroke="#fff" stroke-width="3" fill="none"/>
    </svg>
    <span class="pageno pageno--right">3</span>
    <span class="web-inside web-inside--right">www.ferngatelegal.com.au</span>
  </article>
  <div class="fold"></div>
</section>

</body>
</html>
```